New Coffee Brand Packaging Design

We need a package design for our new coffee brand called Harkvale Coffee. Our brand mission will be displayed on the packaging (along the side or the back) and we currently have a logo that should be displayed on the front. Feel free to suggest a new logo design as you are designing the packaging if it doesn't fit with your vision. The final design should be creative and conservative. We like coffee colors (dark and light browns, white, cream, black, gold). We also like chalkboard art imagery (i.e. coffee cups, theme words from our mission, people, etc.). One famous person from West Louisville, KY is Cornelius Bray (world famous boxer and activist). If there is a way to draw his image in more of an abstract way where it doesn't infringe any patents that would be the sort of creativity we would like in the packaging. Our coffee brand prides itself on being a coffee for the people. For the average joe, working American who enjoys a good cup of coffee and a good atmosphere.

Harkvale Coffee Mission: "We aim to be a coffee company for the people. The people who have an appreciation and love for family, community and who never forget where they came from. Our coffee was born out of West Louisville, KY…a place like many others where the hearts, the minds and the wills are strong. We hope you enjoy each and every cup. Peace & Blessings."

Reason: Extending the deadline to see if there are more design ideas.

Requirements
Must have
• (On the side or on the back of the packaging) Harkvale Coffee Mission: "We aim to be a coffee company for the people. The people who have an appreciation and love for family, community and who never forget where they came from. Our coffee was born out of West Louisville, KY…a place like many others where the hearts, the minds and the wills are strong. We hope you enjoy each and every cup. Peace & Blessings."
Nice to have
• Coffee Colors: dark and light browns, white, cream, black, gold

```html
<!DOCTYPE html>
<html lang="en">
<head>
<meta charset="utf-8">
<title>Harkvale Coffee – Package Panel</title>
<link href="https://fonts.googleapis.com/css2?family=Archivo:wght@700&family=Archivo+Black&family=Oswald:wght@500&display=swap" rel="stylesheet">
<style>
  :root {
    --backdrop: #1a1512;
    --kraft: #c9a57a;
    --kraft-light: #d2b088;
    --kraft-shade: #b48f65;
    --kraft-side: #a98560;
    --ink: #15110d;
    --ink-soft: #3a2c20;
    --stitch: #9c6a2e;
    --portrait-dark: #1f1711;
    --portrait-mid: #6e5640;
  }
  * { margin: 0; padding: 0; box-sizing: border-box; }
  html, body { width: 1200px; height: 1200px; overflow: hidden; background: var(--backdrop); }
  .canvas { position: relative; width: 1200px; height: 1200px; }

  .side-panel {
    position: absolute; left: 270px; top: 100px; width: 96px; height: 1020px;
    background: linear-gradient(90deg, var(--kraft-side), var(--kraft-shade));
  }
  .mission-statement {
    position: absolute; left: 10px; top: 330px; width: 78px;
    font-family: "Oswald", sans-serif; font-weight: 500; font-size: 10.5px;
    line-height: 1.32; letter-spacing: 0.2px; text-transform: uppercase;
    color: var(--ink-soft);
  }

  .front-panel {
    position: absolute; left: 366px; top: 100px; width: 564px; height: 1020px;
    background: linear-gradient(180deg, var(--kraft) 0%, var(--kraft-light) 55%, var(--kraft-shade) 100%);
    overflow: hidden;
  }
  .stitch-line {
    position: absolute; left: 40px; right: 16px; top: 22px;
    border-top: 3px dotted var(--stitch);
  }
  .portrait {
    position: absolute; left: 110px; top: 34px; width: 454px; height: 716px;
  }
  .origin-line {
    position: absolute; left: 150px; top: 84px; width: 330px;
    font-family: "Archivo", sans-serif; font-weight: 700; font-size: 18px;
    line-height: 1.35; letter-spacing: 0.6px; text-align: center;
    color: var(--kraft-light);
  }
  .origin-line small { font-size: 14px; }

  .brand-block {
    position: absolute; left: 60px; top: 780px; width: 360px; text-align: center;
    color: var(--ink);
  }
  .brand-dot {
    width: 34px; height: 34px; border-radius: 50%; background: var(--ink);
    margin: 0 auto 14px;
  }
  .brand-name {
    font-family: "Archivo Black", sans-serif; font-size: 58px; line-height: 0.95;
    text-transform: uppercase; letter-spacing: 0.5px;
  }
  .brand-name .first { display: block; font-size: 40px; margin-bottom: 4px; }
  .quality-band {
    display: inline-block; margin-top: 12px; padding: 6px 26px;
    background: var(--ink); color: var(--kraft);
    font-family: "Archivo", sans-serif; font-weight: 700; font-size: 15px; letter-spacing: 0.8px;
  }
  .founded {
    margin-top: 14px; font-family: "Archivo", sans-serif; font-weight: 700;
    font-size: 11px; letter-spacing: 0.5px;
  }
</style>
</head>
<body>
<main class="canvas">
  <section class="side-panel">
    <p class="mission-statement">We aim to be a coffee company for the people. The people who have an appreciation and love for family, community and who never forget where they came from. Our coffee was born out of West Louisville, KY… a place like many others where the hearts, the minds and the wills are strong. We hope you enjoy each and every cup. Peace &amp; Blessings.</p>
  </section>

  <section class="front-panel">
    <div class="stitch-line"></div>

    <svg class="portrait" viewBox="0 0 454 716" preserveAspectRatio="none" role="img" aria-label="Halftone engraved portrait of boxer Cornelius Bray, head and shoulders, looking sideways">
      <defs>
        <linearGradient id="portraitTone" x1="0" y1="0" x2="0" y2="1">
          <stop offset="0" stop-color="var(--portrait-dark)"/>
          <stop offset="0.28" stop-color="var(--portrait-mid)"/>
          <stop offset="0.75" stop-color="#a8875f"/>
          <stop offset="1" stop-color="#c2a078" stop-opacity="0"/>
        </linearGradient>
      </defs>
      <rect x="0" y="0" width="454" height="716" fill="url(#portraitTone)"/>
    </svg>

    <p class="origin-line">ANOTHER GREATNESS <small>FROM</small><br>WEST LOUISVILLE, KY</p>

    <div class="brand-block">
      <div class="brand-dot"></div>
      <h1 class="brand-name"><span class="first">Harkvale</span>Coffee</h1>
      <div class="quality-band">PREMIUM QUALITY</div>
      <p class="founded">SINCE 1900</p>
    </div>
  </section>
</main>
</body>
</html>
```